Income Tax Flyer - Updates Needed

Just need to update this flyer design and give it a new look. We would like to keep all the same wording but make it stand out a little more. Our selling point is the "Same Day Tax Advance up to $6,000"

Industry/Entity Type

Lending, Small Loans, Tax Services, Title Loans, Personal Loans

```html
<!DOCTYPE html>
<html lang="en">
<head>
<meta charset="utf-8">
<title>Same Day Tax Advance – Brindlemoor Tax &amp; Lending</title>
<link rel="stylesheet" href="https://fonts.googleapis.com/css2?family=Noto+Serif:wght@400;700;800&display=swap">
<style>
  :root {
    --green: #17553a;
    --red: #c42128;
    --white: #ffffff;
  }
  * { margin: 0; padding: 0; box-sizing: border-box; }
  html, body { width: 929px; height: 1200px; overflow: hidden; background: var(--white); }
  body { font-family: "Noto Serif", Georgia, serif; }
  .flyer { position: relative; width: 929px; height: 1200px; overflow: hidden; background: var(--white); }
  .shapes { position: absolute; inset: 0; }
  .brand {
    position: absolute; left: 50px; top: 88px; width: 185px;
    color: var(--green); font-weight: 700; line-height: 1.15; text-align: center;
  }
  .brand-name { display: block; font-size: 27px; }
  .brand-sub { display: block; font-size: 11px; letter-spacing: 3px; }
  .headline {
    position: absolute; left: 52px; top: 198px;
    color: var(--red); font-weight: 800; font-size: 58px; line-height: 75px;
    letter-spacing: -0.5px;
  }
  .benefit {
    position: absolute; left: 0; width: 922px; height: 62px;
    color: var(--white); font-weight: 800; font-size: 34px; line-height: 62px;
    text-align: center; letter-spacing: -0.3px;
  }
  .benefit-speed { top: 577px; }
  .benefit-amount { top: 651px; }
  .benefit-ease { top: 725px; }
  .cta {
    position: absolute; left: 52px; top: 850px;
    color: var(--white); font-size: 56px; line-height: 73px; font-weight: 400;
  }
  .cta strong { font-weight: 800; font-size: 50px; }
  .contact {
    position: absolute; right: 28px; top: 860px;
    color: var(--white); font-weight: 800; text-align: right;
  }
  .contact-title { font-size: 49px; line-height: 64px; }
  .contact-phone { font-size: 43px; line-height: 50px; margin-right: 22px; }
  .contact-line { font-size: 35px; line-height: 45px; margin-right: 26px; }
</style>
</head>
<body>
<main class="flyer">
  <svg class="shapes" width="929" height="1200" viewBox="0 0 929 1200">
    <defs>
      <linearGradient id="topGradient" gradientUnits="userSpaceOnUse" x1="344" y1="0" x2="929" y2="0">
        <stop offset="0" stop-color="#17553a"/>
        <stop offset="1" stop-color="#c42128"/>
      </linearGradient>
      <linearGradient id="bottomGradient" gradientUnits="userSpaceOnUse" x1="0" y1="0" x2="680" y2="0">
        <stop offset="0" stop-color="#17553a"/>
        <stop offset="1" stop-color="#c42128"/>
      </linearGradient>
      <linearGradient id="bandGradient" gradientUnits="userSpaceOnUse" x1="0" y1="0" x2="922" y2="0">
        <stop offset="0" stop-color="#17553a"/>
        <stop offset="1" stop-color="#c42128"/>
      </linearGradient>
      <linearGradient id="photoTone" x1="0" y1="0" x2="0" y2="1">
        <stop offset="0" stop-color="#e6e4df"/>
        <stop offset="0.55" stop-color="#d9c6ad"/>
        <stop offset="1" stop-color="#b98a5f"/>
      </linearGradient>
    </defs>

    <polygon class="top-accent" points="344,0 929,0 929,496" fill="url(#topGradient)"/>
    <polygon class="photo-frame" points="683,78 890,198 890,441 683,561 474,441 474,198" fill="#ffffff"/>
    <polygon class="team-photo" role="img" aria-label="Photo of a small team meeting around an office table with laptops and coffee"
             points="683,86 883,202 883,437 683,553 481,437 481,202" fill="url(#photoTone)"/>

    <polygon class="bottom-accent" points="0,612 660,1200 0,1200" fill="url(#bottomGradient)"/>
    <polygon class="contact-panel" points="232,798 922,798 922,1200 690,1200" fill="#c42128"/>

    <rect class="band band-solid" x="0" y="577" width="922" height="62" fill="#c42128"/>
    <rect class="band band-gradient" x="0" y="651" width="922" height="62" fill="url(#bandGradient)"/>
    <rect class="band band-solid" x="0" y="725" width="922" height="62" fill="#c42128"/>
  </svg>

  <div class="brand">
    <span class="brand-name">Brindlemoor</span>
    <span class="brand-sub">TAX &amp; LENDING</span>
  </div>

  <h1 class="headline">Same Day<br>Tax Advance<br>up to $6,000</h1>

  <p class="benefit benefit-speed">Available In 24 Hours or Less</p>
  <p class="benefit benefit-amount">Choose Your Loan Amount</p>
  <p class="benefit benefit-ease">Quick and Easy</p>

  <p class="cta">File your<br>taxes and<br>apply for an<br><strong>Easy Advance!</strong></p>

  <div class="contact">
    <p class="contact-title">Contact Us Today!</p>
    <p class="contact-phone">Phone Number</p>
    <p class="contact-line">Address line 1</p>
    <p class="contact-line">Address line 2</p>
    <p class="contact-line">Address line 3</p>
  </div>
</main>
</body>
</html>
```